We need logo design and homepage fora new company based in Estonia called "Tallow Crest Supply". We sell railway parts.

Page should look a little like www.corvintal-brask.com

Target market is Estonia and railway builders in Baltic States.

Preferred colour combination may be brown/white.

We need more pages: Company profile/ Productcs / About US

Maybe you can add random railway pictures.

Texts and other pictures we will add later, we dont have any of them right now.

Target Market(s)

Logo Text

Tallow Crest Supply

Number of Pages Required

3 page

Font styles to use
Sans Serif

Colors

Designer to choose colors to be used in the design.

Requirements
Must have
• Must have a proper and elegant start page

```html
<!DOCTYPE html>
<html lang="en">
<head>
<meta charset="utf-8">
<title>Tallow Crest Supply</title>
<link rel="stylesheet" href="https://fonts.googleapis.com/css2?family=Merriweather:wght@300;400&family=Poppins:wght@400;500&display=swap">
<style>
:root{
  --brown:#5b3505;
  --brown-dark:#3a2308;
  --heading:#5a3812;
  --text-muted:#a9a9a9;
  --text-dark:#1e1e1e;
  --light:#f2f2f2;
  --white:#ffffff;
  --field-border:#e2e2e2;
}
*{box-sizing:border-box;margin:0;padding:0}
html,body{width:1200px;height:3255px;overflow:hidden}
body{font-family:"Merriweather",Georgia,serif;color:var(--text-dark);background:var(--white);position:relative}

/* Hero */
.hero{position:absolute;top:0;left:0;width:1200px;height:573px;color:var(--white)}
.hero-photo{position:absolute;inset:0;background:linear-gradient(180deg,#3e2a12 0%,#5a3d17 40%,#4b3314 70%,#2f200c 100%)}
.topbar{position:absolute;top:14px;left:243px;width:714px;height:26px;font-family:"Poppins",Arial,sans-serif;font-size:10px;white-space:nowrap}
.search{position:absolute;left:0;top:0;width:192px;height:26px;border:1px solid rgba(255,255,255,.8);border-radius:13px;padding:0 12px;line-height:24px;font-size:10px}
.search svg{position:absolute;right:8px;top:6px}
.connect-group{position:absolute;left:308px;top:0;height:26px;display:flex;align-items:center;gap:10px}
.connect{font-size:9px;line-height:1}
.socials{display:flex;gap:7px}
.socials span{width:7px;height:7px;border-radius:50%;background:var(--white)}
.cart{position:absolute;left:600px;top:0;height:26px;display:flex;align-items:center;gap:8px;font-size:10px;line-height:1}
.cart b{font-weight:500}
.brand{position:absolute;top:62px;left:243px;font-size:25px;font-weight:400}
.nav{position:absolute;top:62px;left:545px;display:flex;align-items:center;font-family:"Poppins",Arial,sans-serif;font-size:13px}
.nav a{color:var(--white);text-decoration:none;padding:8px 16px;margin-right:4px}
.nav a.active{border:1px solid rgba(255,255,255,.85);border-radius:18px;padding:8px 22px}
.hero-title{position:absolute;top:312px;width:100%;text-align:center;font-size:36px;font-weight:400}
.btn-ghost{position:absolute;top:390px;left:508px;width:184px;height:50px;border:1px solid rgba(255,255,255,.85);border-radius:25px;text-align:center;line-height:48px;font-size:17px}

/* Shared */
.section-title{position:absolute;width:100%;text-align:center;font-size:34px;font-weight:400;color:var(--heading)}
.btn{position:absolute;background:var(--brown);color:var(--white);text-align:center;border-radius:26px}

/* Profile */
.profile-photo{position:absolute;left:163px;top:800px;width:386px;height:348px;background:radial-gradient(ellipse at 40% 45%,#a0451c 0%,#6d3a18 35%,#4a3018 70%,#3b2912 100%)}
.profile-text{position:absolute;left:584px;top:796px;width:372px}
.profile-text h3{font-size:25px;font-weight:400;color:var(--text-dark);margin-bottom:30px}
.profile-text p{font-size:12.5px;line-height:23.5px;color:var(--text-muted);font-weight:300;margin-bottom:23px}

/* Products */
.products{position:absolute;top:1367px;left:0;width:1200px;height:621px;background:var(--light)}
.card{position:absolute;top:180px;width:224px;height:358px;background:var(--white);text-align:center}
.card-photo{height:178px}
.card h4{font-size:13px;font-weight:400;color:var(--heading);margin-top:18px}
.card p{font-size:12px;line-height:20px;color:var(--text-muted);font-weight:300;margin:8px auto 0;width:170px}
.card .btn{position:absolute;left:50px;top:288px;width:124px;height:34px;line-height:34px;font-size:11px;border-radius:17px}

/* About */
.about{position:absolute;top:1988px;left:0;width:1200px;height:534px;color:var(--white)}
.about-photo{position:absolute;inset:0;background:linear-gradient(90deg,#3a2412 0%,#4a2e16 45%,#5e3a1a 75%,#3c2612 100%)}
.about h2{position:absolute;top:88px;width:100%;text-align:center;font-size:34px;font-weight:400}
.about-text{position:absolute;top:210px;left:262px;width:676px;text-align:center;font-size:12.5px;line-height:23px;font-weight:300}
.about-text p{margin-bottom:19px}

/* Contact */
.field{position:absolute;border:1px solid var(--field-border);background:var(--white);font-size:11px;padding:16px 13px;color:#444}
.field.msg{padding:14px 13px}

/* Footer */
.footer{position:absolute;top:3034px;left:0;width:1200px;height:221px;background:var(--light);text-align:center}
.footer h5{position:absolute;top:62px;width:100%;font-size:25px;font-weight:400;color:var(--text-dark)}
.footer-nav{position:absolute;top:128px;width:100%;display:flex;justify-content:center;gap:38px;font-family:"Poppins",Arial,sans-serif;font-size:12px}
.copyright{position:absolute;top:160px;width:100%;font-family:"Poppins",Arial,sans-serif;font-size:11.5px}
</style>
</head>
<body>

<header class="hero">
  <div class="hero-photo" role="img" aria-label="Freight locomotive pulling a long train along tracks at dusk, toned in sepia brown"></div>
  <div class="topbar">
    <div class="search">Search
      <svg width="12" height="12" viewBox="0 0 12 12" fill="none" stroke="#fff" stroke-width="1.5"><circle cx="5" cy="5" r="3.5"/><line x1="7.6" y1="7.6" x2="11" y2="11"/></svg>
    </div>
    <div class="connect-group">
      <span class="connect">Connect With Us</span>
      <div class="socials"><span></span><span></span><span></span><span></span><span></span></div>
    </div>
    <div class="cart">
      <svg width="14" height="16" viewBox="0 0 14 16" fill="none" stroke="#fff" stroke-width="1.3"><rect x="1.5" y="5" width="11" height="10"/><path d="M4.5 5V3.5a2.5 2.5 0 0 1 5 0V5"/></svg>
      <span><b>My Cart</b> ( 0 Items )</span>
    </div>
  </div>
  <div class="brand">Tallow Crest Supply</div>
  <nav class="nav">
    <a class="active">Home</a><a>Profile</a><a>Products</a><a>About Us</a><a>Contact Us</a>
  </nav>
  <h1 class="hero-title">Tallow Crest Supply</h1>
  <div class="btn-ghost">Shop Now</div>
</header>

<section class="profile">
  <h2 class="section-title" style="top:688px">Profile</h2>
  <div class="profile-photo" role="img" aria-label="Orange diesel locomotive in motion, blurred with speed"></div>
  <div class="profile-text">
    <h3>Tallow Crest Supply</h3>
    <p>Sed ut perspiciatis unde omnis iste natus error sit voluptatem accusantium doloremque laudantium, totam rem aperiam, eaque ipsa quae ab illo inventore veritatis et quasi architecto beatae vitae dicta sunt explicabo. Nemo enim ipsam voluptatem quia voluptas sit aspernatur aut odit aut fugit, sed quia consequuntur magni dolores eos qui ratione voluptatem sequi nesciunt. Neque porro quisquam est, qui dolorem ipsum quia dolor sit amet, consectetur</p>
    <p>Sed ut perspiciatis unde omnis iste natus error sit voluptatem accusantium doloremque laudantium, totam rem aperiam, eaque ipsa quae ab illo</p>
  </div>
  <div class="btn" style="left:508px;top:1233px;width:184px;height:48px;line-height:48px;font-size:16px">Read More</div>
</section>

<section class="products">
  <h2 class="section-title" style="top:90px">Products</h2>
  <div class="card" style="left:243px">
    <div class="card-photo" role="img" aria-label="Close view of industrial railway machinery parts" style="background:linear-gradient(135deg,#5a5e62,#2f3236 60%,#6a4a3a)"></div>
    <h4>Railway Parts 1</h4>
    <p>Sed ut perspiciatis unde omnis iste natus error</p>
    <div class="btn">Shop Now</div>
  </div>
  <div class="card" style="left:486px">
    <div class="card-photo" role="img" aria-label="Black and white railway switch with converging tracks" style="background:linear-gradient(160deg,#8a8a8a,#3e3e3e 55%,#9a9a9a)"></div>
    <h4>Railway Parts 1</h4>
    <p>Sed ut perspiciatis unde omnis iste natus error</p>
    <div class="btn">Shop Now</div>
  </div>
  <div class="card" style="left:727px">
    <div class="card-photo" role="img" aria-label="Black and white steam locomotive wheels and drive rods" style="background:radial-gradient(circle at 55% 45%,#7a7a7a,#2a2a2a 60%,#111)"></div>
    <h4>Railway Parts 1</h4>
    <p>Sed ut perspiciatis unde omnis iste natus error</p>
    <div class="btn">Shop Now</div>
  </div>
</section>

<section class="about">
  <div class="about-photo" role="img" aria-label="Freight locomotive on parallel tracks in a rail yard, toned in warm brown"></div>
  <h2>About Us</h2>
  <div class="about-text">
    <p>Sed ut perspiciatis unde omnis iste natus error sit voluptatem accusantium doloremque laudantium, totam rem aperiam, eaque ipsa quae ab illo inventore veritatis et quasi architecto beatae vitae dicta sunt explicabo. Nemo enim ipsam voluptatem quia voluptas sit aspernatur aut odit aut fugit, sed quia consequuntur magni dolores eos qui ratione voluptatem sequi nesciunt.</p>
    <p>Sed ut perspiciatis unde omnis iste natus error sit voluptatem accusantium doloremque laudantium, totam rem aperiam, eaque ipsa quae ab illo</p>
  </div>
</section>

<section class="contact">
  <h2 class="section-title" style="top:2582px">Contact us</h2>
  <div class="field" style="left:243px;top:2712px;width:345px;height:50px">Name</div>
  <div class="field" style="left:243px;top:2775px;width:345px;height:50px">E-mail</div>
  <div class="field" style="left:243px;top:2838px;width:345px;height:50px">Phone</div>
  <div class="field msg" style="left:608px;top:2712px;width:345px;height:176px">Message</div>
  <div class="btn" style="left:538px;top:2914px;width:124px;height:32px;line-height:32px;font-size:12px;border-radius:16px">Submit</div>
</section>

<footer class="footer">
  <h5>Tallow Crest Supply</h5>
  <div class="footer-nav"><span>Home</span><span>Profile</span><span>Products</span><span>About Us</span><span>Contact Us</span></div>
  <div class="copyright">© 2017 Company Name &nbsp;|&nbsp; All Rights Reserved</div>
</footer>

</body>
</html>
```